Pelverhook LLC
Business Cards & Stationary
Professional
Tobias Wendell
President
482 Orchard Crest Road
Dunmore Falls, NJ 07934-2718
tobias.wendell@mailvexo.com
www.pelverhook.com
I require the full suite of stationary products i.e.:- Business card, letterhead, envelope, fax cover sheet, thank you cards, invoice etc.
Just the logo on the back of the card.

```html
<!DOCTYPE html>
<html lang="en">
<head>
<meta charset="utf-8">
<title>Pelverhook LLC Stationery Suite</title>
<link rel="stylesheet" href="https://fonts.googleapis.com/css2?family=Open+Sans:wght@400;600;700&display=swap">
<style>
  :root{
    --stage:#e9ecef;
    --paper:#ffffff;
    --blue-deep:#16457f;
    --blue:#2677c2;
    --blue-light:#6cb6e8;
    --ink:#3a3f45;
    --grey:#8b9199;
    --rule:#d5d9de;
    --font:"Open Sans", Arial, sans-serif;
  }
  *{box-sizing:border-box;margin:0;padding:0}
  html,body{width:1200px;height:655px;overflow:hidden}
  body{background:var(--stage);font-family:var(--font);color:var(--ink);position:relative}
  .piece{position:absolute;background:var(--paper);box-shadow:0 2px 8px rgba(0,0,0,.18);overflow:hidden}
  .piece svg.art{position:absolute;left:0;top:0;width:100%;height:100%}
  .brand{position:absolute;display:flex;align-items:center;gap:5px;font-weight:700;color:var(--blue-deep);letter-spacing:.06em;text-transform:uppercase}
  .brand .dot{border-radius:50%;background:var(--blue)}
  .small{font-size:6.5px;line-height:1.45;color:var(--grey)}
  .web{position:absolute;color:#fff;font-size:7px;letter-spacing:.04em}

  /* business cards */
  .card{left:30px;width:270px;height:155px;border-radius:6px}
  .card--front{top:40px}
  .card--back-blue{top:250px;background:var(--blue)}
  .card--back-white{top:460px}
  .card--front .brand{left:16px;top:22px;font-size:11px}
  .card--front .brand .dot{width:14px;height:14px}
  .card__person{position:absolute;right:16px;top:18px;text-align:right}
  .card__name{font-size:10px;font-weight:700;color:var(--blue-deep)}
  .card__title{font-size:7px;color:var(--grey);margin-bottom:6px}
  .card--front .web{left:16px;bottom:7px}
  .card-back__brand{position:absolute;left:0;right:0;top:64px;display:flex;justify-content:center;align-items:center;gap:7px;font-weight:700;font-size:17px;letter-spacing:.08em;text-transform:uppercase}
  .card--back-blue .card-back__brand{color:#fff}
  .card--back-blue .dot{width:18px;height:18px;border-radius:50%;background:#fff}
  .card--back-white .card-back__brand{color:var(--blue-deep)}
  .card--back-white .dot{width:18px;height:18px;border-radius:50%;background:var(--blue)}

  /* letterhead */
  .letterhead{left:325px;top:60px;width:380px;height:537px}
  .letterhead .brand{left:28px;top:30px;font-size:12px}
  .letterhead .brand .dot{width:16px;height:16px}
  .letterhead__contact{position:absolute;right:28px;top:26px;text-align:right}
  .letterhead__watermark{position:absolute;left:110px;top:330px;width:160px;height:120px;border-radius:80px 80px 0 0;background:linear-gradient(180deg,rgba(38,119,194,.07),rgba(38,119,194,.02))}
  .letterhead .web{left:0;right:0;bottom:6px;text-align:center}

  /* fax cover */
  .fax{left:725px;top:22px;width:200px;height:280px}
  .fax .brand{left:14px;top:16px;font-size:8px}
  .fax .brand .dot{width:10px;height:10px}
  .fax__contact{position:absolute;right:14px;top:14px;text-align:right;font-size:5px}
  .fax__fields{position:absolute;left:14px;right:14px;top:62px}
  .fax__field{display:flex;font-size:6px;color:var(--ink);border-bottom:1px solid var(--rule);padding:4px 0}
  .fax__field span{width:34px;font-weight:600}
  .fax__checks{position:absolute;left:14px;right:14px;top:178px;display:flex;flex-wrap:wrap;gap:6px 10px}
  .fax__check{display:flex;align-items:center;gap:3px;font-size:5.5px}
  .fax__check i{width:6px;height:6px;border:1px solid var(--grey)}
  .fax .web{left:0;right:0;bottom:3px;text-align:center;font-size:5px}

  /* envelopes */
  .envelope{left:740px;width:440px;height:150px}
  .envelope--back{top:318px}
  .envelope--front{top:484px}
  .envelope-back__brand{position:absolute;left:0;right:0;top:22px;display:flex;justify-content:center;align-items:center;gap:5px;color:#fff;font-weight:700;font-size:10px;letter-spacing:.08em;text-transform:uppercase}
  .envelope-back__brand .dot{width:12px;height:12px;border-radius:50%;background:#fff}
  .envelope--front .brand{left:20px;top:38px;font-size:11px}
  .envelope--front .brand .dot{width:14px;height:14px}
  .envelope__address{position:absolute;left:20px;top:58px}
  .envelope--front .web{left:0;right:0;bottom:5px;text-align:center}
</style>
</head>
<body>

<!-- business card: front -->
<section class="piece card card--front">
  <svg class="art" viewBox="0 0 270 155" preserveAspectRatio="none" aria-hidden="true">
    <defs><linearGradient id="bandCard" x1="0" x2="1"><stop offset="0" stop-color="#16457f"/><stop offset="1" stop-color="#6cb6e8"/></linearGradient></defs>
    <path d="M0 128 Q140 104 270 118 L270 155 L0 155Z" fill="#6cb6e8" opacity=".45"/>
    <path d="M0 136 Q140 116 270 126 L270 155 L0 155Z" fill="url(#bandCard)"/>
  </svg>
  <div class="brand"><span class="dot"></span>Pelverhook</div>
  <div class="card__person">
    <div class="card__name">Tobias Wendell</div>
    <div class="card__title">President</div>
    <div class="small">482 Orchard Crest Road<br>Dunmore Falls, NJ 07934-2718<br>Phone: 201 555 0148<br>Fax: 201 555 0149<br>tobias.wendell@mailvexo.com</div>
  </div>
  <div class="web">www.pelverhook.com</div>
</section>

<!-- business card: back, blue -->
<section class="piece card card--back-blue">
  <svg class="art" viewBox="0 0 270 155" preserveAspectRatio="none" aria-hidden="true">
    <defs><linearGradient id="bgBlue" x1="0" y1="0" x2="1" y2="1"><stop offset="0" stop-color="#6cb6e8"/><stop offset="1" stop-color="#16457f"/></linearGradient></defs>
    <rect width="270" height="155" fill="url(#bgBlue)"/>
    <path d="M0 120 Q140 92 270 112 L270 155 L0 155Z" fill="#fff" opacity=".9"/>
    <path d="M0 134 Q140 112 270 126 L270 155 L0 155Z" fill="#16457f"/>
  </svg>
  <div class="card-back__brand"><span class="dot"></span>Pelverhook</div>
</section>

<!-- business card: back, white -->
<section class="piece card card--back-white">
  <svg class="art" viewBox="0 0 270 155" preserveAspectRatio="none" aria-hidden="true">
    <defs><linearGradient id="bandWhite" x1="0" x2="1"><stop offset="0" stop-color="#16457f"/><stop offset="1" stop-color="#2677c2"/></linearGradient></defs>
    <path d="M0 124 Q140 98 270 114 L270 155 L0 155Z" fill="url(#bandWhite)"/>
  </svg>
  <div class="card-back__brand"><span class="dot"></span>Pelverhook</div>
</section>

<!-- letterhead -->
<section class="piece letterhead">
  <svg class="art" viewBox="0 0 380 537" preserveAspectRatio="none" aria-hidden="true">
    <defs><linearGradient id="bandLetter" x1="0" x2="1"><stop offset="0" stop-color="#16457f"/><stop offset="1" stop-color="#2677c2"/></linearGradient></defs>
    <path d="M0 500 Q190 480 380 498 L380 537 L0 537Z" fill="#6cb6e8" opacity=".35"/>
    <path d="M0 514 Q190 500 380 512 L380 537 L0 537Z" fill="url(#bandLetter)"/>
  </svg>
  <div class="brand"><span class="dot"></span>Pelverhook</div>
  <div class="letterhead__contact small">482 Orchard Crest Road<br>Dunmore Falls, NJ 07934-2718<br>Phone: 201 555 0148<br>Fax: 201 555 0149<br>tobias.wendell@mailvexo.com</div>
  <div class="letterhead__watermark" role="img" aria-label="Faint brand decoration area"></div>
  <div class="web">www.pelverhook.com</div>
</section>

<!-- fax cover sheet -->
<section class="piece fax">
  <svg class="art" viewBox="0 0 200 280" preserveAspectRatio="none" aria-hidden="true">
    <rect x="0" y="268" width="200" height="12" fill="#16457f"/>
  </svg>
  <div class="brand"><span class="dot"></span>Pelverhook</div>
  <div class="fax__contact small">482 Orchard Crest Road<br>Dunmore Falls, NJ 07934-2718<br>Phone: 201 555 0148<br>Fax: 201 555 0149</div>
  <div class="fax__fields">
    <div class="fax__field"><span>To:</span></div>
    <div class="fax__field"><span>From:</span></div>
    <div class="fax__field"><span>Fax:</span></div>
    <div class="fax__field"><span>Pages:</span></div>
    <div class="fax__field"><span>Date:</span></div>
    <div class="fax__field"><span>Re:</span></div>
  </div>
  <div class="fax__checks">
    <div class="fax__check"><i></i>Urgent</div>
    <div class="fax__check"><i></i>For Review</div>
    <div class="fax__check"><i></i>Please Comment</div>
    <div class="fax__check"><i></i>Please Reply</div>
    <div class="fax__check"><i></i>Please Recycle</div>
  </div>
  <div class="web">www.pelverhook.com</div>
</section>

<!-- envelope: back with flap -->
<section class="piece envelope envelope--back">
  <svg class="art" viewBox="0 0 440 150" preserveAspectRatio="none" aria-hidden="true">
    <defs><linearGradient id="flap" x1="0" y1="0" x2="0" y2="1"><stop offset="0" stop-color="#2677c2"/><stop offset="1" stop-color="#6cb6e8"/></linearGradient></defs>
    <path d="M0 0 L440 0 L440 14 Q330 40 240 70 Q220 78 200 70 Q110 40 0 14Z" fill="url(#flap)"/>
    <path d="M0 150 L200 80 Q220 74 240 80 L440 150" fill="none" stroke="#d5d9de"/>
  </svg>
  <div class="envelope-back__brand"><span class="dot"></span>Pelverhook</div>
</section>

<!-- envelope: front -->
<section class="piece envelope envelope--front">
  <svg class="art" viewBox="0 0 440 150" preserveAspectRatio="none" aria-hidden="true">
    <defs><linearGradient id="bandEnv" x1="0" x2="1"><stop offset="0" stop-color="#16457f"/><stop offset="1" stop-color="#2677c2"/></linearGradient></defs>
    <path d="M250 0 Q350 6 440 28 L440 0Z" fill="#6cb6e8"/>
    <path d="M0 128 Q220 112 440 126 L440 150 L0 150Z" fill="url(#bandEnv)"/>
  </svg>
  <div class="brand"><span class="dot"></span>Pelverhook</div>
  <div class="envelope__address small">482 Orchard Crest Road<br>Dunmore Falls, NJ 07934-2718</div>
  <div class="web">www.pelverhook.com</div>
</section>

</body>
</html>
```